Facebook Cover & Profile Branding for VelbrooK Systems

We need a modern, premium Facebook cover image for our company Velbrook Systems GmbH. The design should be clean, professional, and aligned with our corporate colors (neon green and deep blue) as well as our logo. It should clearly represent us as a technology and IT consulting company with a strong focus on software testing and quality assurance.

Since Velbrook Systems is also active in the U.S. market, the design may include global or U.S.-related elements (e.g., subtle references to international presence, tech innovation with a global reach).

Requirements:

Integration of the Velbrook logo and brand colors

Modern, premium look with a tech-driven feel

Clear, simple layout that looks good on desktop and mobile

Optional: subtle U.S./international references to highlight our global presence

Goal:
A professional, eye-catching Facebook cover image that strengthens our brand identity and reflects our international expansion into the U.S. market.

Target Market(s)

Medium to large enterprises in the technology, finance, and energy sectors - Companies looking for premium IT consulting, software testing, and quality assurance services - Decision makers and executives (CIOs, CTOs, IT managers) in Europe and the United States - A global audience that values innovation, professionalism, and trust

Industry/Entity Type

Information Technology & Consulting Software Testing & Quality Assurance Technology / Professional Services Global IT Consulting with U.S. Market Presence

Requirements
Must have
• Integration of the Velbrook Systems logo and brand colors (Neon Green & Deep Blue) Modern, premium design with a strong tech-oriented look and feel Clean and professional layout, optimized for both desktop and mobile display Clear visibility of the brand identity (technology, IT consulting, software testing, quality assurance) Subtle reference to U.S. presence / global expansion (to highlight activity in both Germany and the U.S.) Balanced use of colors and space for a high-end, corporate appearance
Nice to have
• Subtle animations or motion effects (e.g., light gradients, moving lines, glowing accents) Dark/Light version option for different moods or seasonal campaigns Integration of social media icons (LinkedIn, Instagram, Facebook) in a clean, minimal way Tech-inspired background elements (digital patterns, abstract shapes, network grids) Space for an optional tagline or slogan (e.g., “Innovation. Quality. Global Impact.”) Adaptability for other platforms (so the design style can be reused for LinkedIn or Twitter headers)
Should not have
• Cluttered or overloaded layouts that reduce clarity Low-quality stock photos or generic imagery that doesn’t fit a premium brand Use of colors outside the Velbrook brand identity (Neon Green & Deep Blue) Outdated design styles (e.g., heavy gradients, 3D effects, drop shadows) Complex text blocks that make the design look busy Elements that distract from the logo and core brand message Pop-art or playful styles that don’t match the premium, professional tech look

```html
<!DOCTYPE html>
<html lang="en">
<head>
<meta charset="utf-8">
<title>Velbrook Systems — Facebook Cover &amp; Profile</title>
<link rel="stylesheet" href="https://fonts.googleapis.com/css2?family=Orbitron:wght@500&family=Exo+2:wght@300;400&display=swap">
<style>
  :root {
    --page: #ffffff;
    --ink: #000000;
    --white: #ffffff;
    --neon-green: #3ee52c;
    --mid-teal: #1fb58a;
    --deep-blue: #1a6de0;
    --glow-green: rgba(62, 229, 44, 0.22);
    --glow-teal: rgba(30, 190, 170, 0.18);
    --glow-blue: rgba(26, 109, 224, 0.16);
  }
  * { margin: 0; padding: 0; box-sizing: border-box; }
  html, body {
    width: 1200px;
    height: 660px;
    overflow: hidden;
    background: var(--page);
  }
  .canvas {
    position: relative;
    width: 1200px;
    height: 660px;
    background: var(--page);
  }
  .cover {
    position: absolute;
    left: 74px;
    top: 74px;
    width: 1054px;
    height: 401px;
    background: var(--ink);
    overflow: hidden;
  }
  .cover-network {
    position: absolute;
    inset: 0;
    background:
      radial-gradient(ellipse 260px 200px at 8% 30%, var(--glow-teal), transparent 70%),
      radial-gradient(ellipse 200px 160px at 15% 85%, var(--glow-green), transparent 70%),
      radial-gradient(ellipse 320px 240px at 78% 15%, var(--glow-green), transparent 70%),
      radial-gradient(ellipse 300px 220px at 70% 70%, var(--glow-teal), transparent 70%),
      radial-gradient(ellipse 200px 200px at 98% 45%, var(--glow-blue), transparent 70%);
  }
  .cover-art {
    position: absolute;
    inset: 0;
  }
  .headline {
    font-family: 'Orbitron', sans-serif;
    font-weight: 500;
    fill: var(--white);
  }
  .tagline {
    font-family: 'Exo 2', sans-serif;
    font-weight: 300;
  }
  .tagline .word-green { fill: var(--neon-green); }
  .tagline .word-blue { fill: var(--mid-teal); }

  .profile {
    position: absolute;
    left: 144px;
    top: 410px;
    width: 236px;
    height: 236px;
    border-radius: 50%;
    background: var(--ink);
    border: 4px solid var(--white);
    box-shadow: 0 0 0 1px var(--ink);
    display: flex;
    flex-direction: column;
    align-items: center;
    justify-content: center;
    color: var(--white);
    font-family: 'Exo 2', sans-serif;
  }
  .profile-dot {
    width: 34px;
    height: 34px;
    border-radius: 50%;
    background: var(--neon-green);
    margin-bottom: 16px;
  }
  .profile-name {
    font-size: 30px;
    font-weight: 400;
    letter-spacing: 3px;
    line-height: 1;
  }
  .profile-sub {
    margin-top: 6px;
    font-size: 14px;
    font-weight: 300;
    letter-spacing: 0.5px;
  }
</style>
</head>
<body>
<main class="canvas">
  <section class="cover">
    <div class="cover-network" role="img" aria-label="Glowing green and teal network lines with connected nodes on black"></div>
    <svg class="cover-art" width="1054" height="401" viewBox="0 0 1054 401" aria-hidden="false">
      <defs>
        <linearGradient id="brand-sweep" x1="0" y1="0" x2="1" y2="0">
          <stop offset="0" stop-color="#3ee52c"/>
          <stop offset="0.55" stop-color="#1fb58a"/>
          <stop offset="1" stop-color="#1a6de0"/>
        </linearGradient>
      </defs>
      <circle class="brand-disc" cx="820" cy="206" r="176" fill="url(#brand-sweep)"/>
      <text class="headline" x="94" y="148" font-size="56" textLength="466" lengthAdjust="spacingAndGlyphs">EMPOWERING</text>
      <text class="headline" x="94" y="209" font-size="56" textLength="462" lengthAdjust="spacingAndGlyphs">TECHNOLOGY</text>
      <text class="tagline" x="192" y="263" font-size="38" textLength="366" lengthAdjust="spacingAndGlyphs"><tspan class="word-green">ENABLING</tspan> <tspan class="word-blue">SUCCESS</tspan></text>
    </svg>
  </section>

  <aside class="profile">
    <span class="profile-dot"></span>
    <span class="profile-name">VELBROOK</span>
    <span class="profile-sub">Velbrook Systems GmbH</span>
  </aside>
</main>
</body>
</html>
```